Pagecraft Design Project

I currently have a temporary website at www.brindlecroftadvisory.com this site provides a good sample of the information which needs to be included on the website. As you will see the design is very basic and does not include the company logo or any reference to the colors of the logo.

A couple of webpages which I really like and should provide an indication:
- quilvo.com
- tarravox.it (good client log in, dont like dark colors)
- pixel harbour
- lumatill.com

I have also added the company logo and my business card which provide some idea of coloring etc.

Requirements
Must have
• - Blog Page - see blog.quilvo.com for a good example;
- Client log-in;
- Twitter linkage;
- linkedin linkage;
- mobile browser scale ability;

```html
<!DOCTYPE html>
<html lang="en">
<head>
<meta charset="utf-8">
<title>Brindlecroft Advisory</title>
<link href="https://fonts.googleapis.com/css2?family=Open+Sans:wght@400;600;700&family=Lora:ital,wght@0,400;1,400;1,700&display=swap" rel="stylesheet">
<style>
:root{
  --blue:#1d8fd1;
  --blue-dark:#13679c;
  --teal:#2b6f84;
  --teal-dark:#1f5466;
  --ink:#333;
  --muted:#777;
  --line:#ddd;
  --paper:#fff;
  --soft:#f4f6f7;
}
*{box-sizing:border-box;margin:0;padding:0}
html,body{width:755px;height:1200px;overflow:hidden;background:var(--paper);font-family:"Open Sans",sans-serif;color:var(--ink)}
.page{width:755px;height:1200px;position:relative}
.site-header{height:56px;display:flex;align-items:center;justify-content:space-between;padding:0 18px}
.brand{display:flex;align-items:center;gap:8px;font-size:19px;font-weight:700;color:var(--blue-dark)}
.brand-dot{width:26px;height:26px;border-radius:50%;background:var(--blue)}
.header-right{text-align:right}
.phone{font-size:15px;font-weight:700;color:var(--ink);display:flex;align-items:center;gap:6px;justify-content:flex-end}
.main-nav{display:flex;gap:4px;margin-top:4px}
.main-nav a{font-size:10px;font-weight:600;color:var(--blue-dark);text-decoration:none;padding:3px 7px}
.main-nav a.active{background:var(--blue);color:#fff}
.hero{position:relative;height:245px;background:linear-gradient(120deg,#c8d3a0 0%,#9fb6a8 35%,#6f8f8a 60%,#c9d2c8 100%)}
.hero-photo{position:absolute;inset:0}
.speech{position:absolute;left:205px;top:18px;width:120px;background:#fff;border-radius:14px;padding:8px 10px;font-family:"Lora",serif;font-size:10px;line-height:1.3;color:#444;box-shadow:0 1px 4px rgba(0,0,0,.25)}
.hero-caption{position:absolute;left:0;right:0;bottom:0;height:34px;background:rgba(30,60,70,.75);color:#fff;font-size:11px;font-weight:700;letter-spacing:.5px;display:flex;align-items:center;justify-content:center}
.welcome{background:var(--soft);padding:20px 40px 18px;text-align:center;height:180px;border-bottom:1px solid var(--line)}
.welcome h1{font-family:"Lora",serif;font-style:italic;font-weight:400;font-size:22px;color:var(--muted)}
.welcome h1 span{color:var(--blue);font-weight:700}
.welcome p{font-family:"Lora",serif;font-style:italic;font-size:10.5px;line-height:1.55;color:#555;margin-top:10px}
.content{display:flex;gap:18px;padding:18px 18px 0;height:540px}
.blog{flex:1}
.section-title{font-family:"Lora",serif;font-style:italic;font-size:20px;color:var(--teal-dark);border-bottom:1px solid var(--line);padding-bottom:6px}
.post{padding:12px 0;border-bottom:1px solid var(--line)}
.post h2{font-size:12px;font-weight:600;color:var(--blue)}
.meta{font-size:8.5px;color:var(--muted);margin:4px 0 8px;display:flex;gap:14px}
.post-body{display:flex;gap:12px}
.thumb{width:170px;height:118px;flex:none;background:linear-gradient(135deg,#b9c6d0,#7e93a3)}
.post-body p{font-size:8.5px;line-height:1.55;color:#555}
.more{display:block;text-align:right;margin-top:6px}
.more span{background:var(--blue);color:#fff;font-size:8.5px;padding:2px 8px}
.sidebar{width:160px}
.login{border:1px solid var(--line)}
.login h3{font-size:12px;color:#fff;background:var(--blue);padding:6px 8px;font-weight:600}
.login form{padding:8px}
.field{height:18px;border:1px solid var(--line);font-size:8px;color:#999;padding:3px 5px;margin-bottom:6px}
.login small{font-size:7.5px;color:var(--muted);display:block;margin-bottom:6px}
.btn{background:var(--blue);color:#fff;font-size:9px;padding:3px 12px;display:inline-block}
.recent{margin-top:18px}
.recent h3{font-size:11px;color:var(--teal-dark);border-bottom:1px solid var(--line);padding-bottom:4px}
.recent li{list-style:none;font-size:7.5px;line-height:1.45;color:var(--muted);padding:6px 0 6px 12px;border-bottom:1px dotted var(--line);position:relative}
.recent li::before{content:"";position:absolute;left:0;top:9px;width:6px;height:6px;background:var(--blue)}
.site-footer{position:absolute;left:0;right:0;top:1020px;height:150px;background:var(--teal);color:#fff;display:flex;padding:18px 34px;gap:20px}
.col{flex:1}
.col h4{font-size:12px;font-weight:700;margin-bottom:8px}
.col p{font-size:8.5px;line-height:1.5;color:#d5e6ec;display:flex;gap:6px;align-items:flex-start}
.col .big{font-size:16px;font-weight:700;color:#fff;align-items:center}
.footer-bar{position:absolute;left:0;right:0;bottom:0;height:30px;background:var(--teal-dark);display:flex;align-items:center;padding:0 34px;gap:16px}
.footer-bar a{font-size:8.5px;color:#fff;text-decoration:none}
</style>
</head>
<body>
<div class="page">
  <header class="site-header">
    <div class="brand"><span class="brand-dot"></span>Brindlecroft Advisory</div>
    <div class="header-right">
      <div class="phone"><svg width="12" height="12" viewBox="0 0 24 24"><path fill="#1d8fd1" d="M6.6 10.8a15 15 0 0 0 6.6 6.6l2.2-2.2c.3-.3.7-.4 1-.2 1.1.4 2.3.6 3.6.6.6 0 1 .4 1 1V20c0 .6-.4 1-1 1A17 17 0 0 1 3 4c0-.6.4-1 1-1h3.5c.6 0 1 .4 1 1 0 1.3.2 2.5.6 3.6.1.3 0 .7-.2 1z"/></svg>0491 682 207</div>
      <nav class="main-nav"><a class="active">Home</a><a>Consulting</a><a>Accounting</a><a>Partners</a><a>About us</a><a>Contact us</a></nav>
    </div>
  </header>

  <section class="hero">
    <div class="hero-photo" role="img" aria-label="Businesswoman in a dark suit standing in a bright glass office lobby"></div>
    <div class="speech">Proin gravida nibh vel velit auctor aliquet. Aenean sollicitudin, lorem quis bibendum auctor, nisi elit consequat ipsum.</div>
    <div class="hero-caption">AENEAN SOLLICITUDIN, LOREM QUIS BIBENDUM AUCTOR, NISI ELIT CONSEQUAT IPSUM.</div>
  </section>

  <section class="welcome">
    <h1>Welcome to <span>Brindlecroft Advisory</span></h1>
    <p>Brindlecroft Advisory is a business advisory firm focused on assisting businesses reach their potential. We understand and are passionate about small and medium sized businesses. Through the provision of sound long term advice we aim to build strong ongoing relationships with our clients.</p>
    <p>We offer business ongoing accounting services and advice, as well as provide consulting services to help businesses through difficult times. As a Chartered Accounting Firm with a strong technical accounting background and considerable experience in assisting business dealing with significant issues within their business, Brindlecroft Advisory can assist your business reach its full potential.</p>
  </section>

  <main class="content">
    <section class="blog">
      <h2 class="section-title">Blog</h2>
      <article class="post">
        <h2>Neque porro quisquam est qui dolorem ipsum quia dolor sit amet.</h2>
        <div class="meta"><span>11.05.14</span><span>Comment (0)</span><span>Published by Ellis R</span></div>
        <div class="post-body">
          <div class="thumb" role="img" aria-label="Team of colleagues gathered around a laptop"></div>
          <div><p>Lorem Ipsum is simply dummy text of the printing and typesetting industry. Lorem Ipsum has been the industry's standard dummy text ever since the 1500s, when an unknown printer took a galley of type and scrambled it to make a type specimen book. It has survived not only five centuries, but also the leap into electronic typesetting, remaining essentially unchanged. It was popularised in the 1960s with the release of Letraset sheets containing Lorem Ipsum passages.</p><span class="more"><span>Read More »</span></span></div>
        </div>
      </article>
      <article class="post">
        <h2>Neque porro quisquam est qui dolorem ipsum quia dolor sit amet.</h2>
        <div class="meta"><span>11.05.14</span><span>Comment (0)</span><span>Published by Ellis R</span></div>
        <div class="post-body">
          <div class="thumb" role="img" aria-label="Group of business people in a meeting room"></div>
          <div><p>Lorem Ipsum is simply dummy text of the printing and typesetting industry. Lorem Ipsum has been the industry's standard dummy text ever since the 1500s, when an unknown printer took a galley of type and scrambled it to make a type specimen book. It has survived not only five centuries, but also the leap into electronic typesetting, remaining essentially unchanged. It was popularised in the 1960s with the release of Letraset sheets containing Lorem Ipsum passages.</p><span class="more"><span>Read More »</span></span></div>
        </div>
      </article>
    </section>
    <aside class="sidebar">
      <div class="login">
        <h3>Login</h3>
        <form>
          <div class="field">Username</div>
          <div class="field">Password</div>
          <small>Forgot your password? · Sign up</small>
          <span class="btn">Login</span>
        </form>
      </div>
      <div class="recent">
        <h3>Recently Commented</h3>
        <ul>
          <li>Clear advice on cash flow planning helped us through a slow quarter this year.</li>
          <li>Great summary of the new tax changes for small business owners in the region.</li>
          <li>Thanks for the tips on bookkeeping, we switched our process last month.</li>
          <li>Looking forward to the next post on growth planning and staff costs.</li>
        </ul>
      </div>
    </aside>
  </main>

  <footer class="site-footer">
    <div class="col"><h4>Contact</h4>
      <p><svg width="10" height="12" viewBox="0 0 24 24"><path fill="#fff" d="M12 2a7 7 0 0 0-7 7c0 5 7 13 7 13s7-8 7-13a7 7 0 0 0-7-7zm0 9.5a2.5 2.5 0 1 1 0-5 2.5 2.5 0 0 1 0 5z"/></svg>Level 2, 14 Harbour Street, Wattle Reach, NSW 2444<br>PO Box 318, Wattle Reach, NSW 2444</p></div>
    <div class="col"><h4>Phone no</h4>
      <p class="big"><svg width="13" height="13" viewBox="0 0 24 24"><path fill="#fff" d="M6.6 10.8a15 15 0 0 0 6.6 6.6l2.2-2.2c.3-.3.7-.4 1-.2 1.1.4 2.3.6 3.6.6.6 0 1 .4 1 1V20c0 .6-.4 1-1 1A17 17 0 0 1 3 4c0-.6.4-1 1-1h3.5c.6 0 1 .4 1 1 0 1.3.2 2.5.6 3.6.1.3 0 .7-.2 1z"/></svg>0491 682 207</p></div>
    <div class="col"><h4>Email</h4>
      <p><svg width="12" height="10" viewBox="0 0 24 18"><rect x="1" y="1" width="22" height="16" fill="none" stroke="#fff" stroke-width="2"/><path d="M1 1l11 9 11-9" fill="none" stroke="#fff" stroke-width="2"/></svg>hello@brindlecroftadvisory.com</p></div>
    <nav class="footer-bar"><a>Home</a><a>Consulting</a><a>Accounting</a><a>Partners</a><a>About us</a><a>Contact us</a></nav>
  </footer>
</div>
</body>
</html>
```